Oil Field Service company needs professional business cards

Looking to clean up our current company business cards and look a little more professional. Harlow Tubular Services is a US based company that services the oil field. We deal with engineers, managers and oil rigs....................................................................................................................................................................................................................................................................................................................................................................................................

Target Market(s)

Oil and Gas professionals

Industry/Entity Type

Oil And Gas

Contact Information for Business Card

See attached photo as example

Font styles to use
Sans Serif

Colors
ec1f27

Requirements
Must have
• Company Logo, Name, Title, Cell, Office, Fax, Email.
• See attached photo
Nice to have
• External CRT, Internal CRT, Casing Crews, Torque Turn, Laydown Machine
Should not have
• Do not introduce any new pictures and keep it professional looking

```html
<!DOCTYPE html>
<html lang="en">
<head>
<meta charset="utf-8">
<title>Harlow Tubular Services – Business Card</title>
<link href="https://fonts.googleapis.com/css2?family=Archivo:wght@800&family=Oswald:wght@300;400&family=Roboto:wght@400;700&display=swap" rel="stylesheet">
<style>
  :root {
    --brand-red: #ec1f27;
    --slate: #3d5262;
    --card-white: #f4f4f4;
    --backdrop: #e4e4e4;
    --text-dark: #333d45;
    --text-light: #ffffff;
    --text-muted: #d9e0e5;
  }
  * { margin: 0; padding: 0; box-sizing: border-box; }
  html, body {
    width: 1200px; height: 576px; overflow: hidden;
    background: var(--backdrop);
  }
  .stage { position: relative; width: 1200px; height: 576px; }
  .card {
    position: absolute; top: 142px;
    width: 484px; height: 292px;
    border-radius: 6px; overflow: hidden;
    background: var(--card-white);
  }
  .card--front { left: 82px; }
  .card--back { left: 634px; background: var(--slate); }

  .wordmark {
    position: absolute; left: 0; right: 0;
    text-align: center; color: var(--slate);
    font-family: "Archivo", "Arial Black", sans-serif; font-weight: 800;
    line-height: 1;
  }
  .wordmark__main { display: block; letter-spacing: 1px; }
  .wordmark__sub { display: block; letter-spacing: 3.5px; }
  .card--front .wordmark { top: 74px; }
  .card--front .wordmark__main { font-size: 54px; }
  .card--front .wordmark__sub { font-size: 17px; margin-top: 16px; }

  .service-band {
    position: absolute; left: 0; right: 0; top: 219px; height: 27px;
    background: var(--brand-red); color: var(--text-light);
    font-family: "Roboto", Arial, sans-serif; font-weight: 700; font-size: 12.5px;
    display: flex; align-items: center; justify-content: center; gap: 7px;
  }
  .website-line {
    position: absolute; left: 0; right: 0; top: 260px;
    display: flex; align-items: center; justify-content: center; gap: 10px;
    font-family: "Roboto", Arial, sans-serif; font-size: 14px; color: var(--text-dark);
  }
  .website-line .rule { display: block; width: 82px; height: 4px; }

  .back-curve { position: absolute; inset: 0; }
  .card--back .wordmark { left: 230px; right: 0; top: 46px; }
  .card--back .wordmark__main { font-size: 38px; }
  .card--back .wordmark__sub { font-size: 13px; margin-top: 12px; letter-spacing: 2.8px; }

  .holder { position: absolute; left: 18px; top: 130px; color: var(--text-light); }
  .holder__name { font-family: "Oswald", sans-serif; font-weight: 400; font-size: 23px; line-height: 1.1; }
  .holder__title { font-family: "Roboto", Arial, sans-serif; font-size: 12px; color: var(--text-muted); margin-top: 3px; }

  .contacts {
    position: absolute; top: 222px; list-style: none;
    font-family: "Oswald", sans-serif; font-weight: 300; font-size: 12.5px;
    color: var(--text-light);
  }
  .contacts--phones { left: 20px; }
  .contacts--details { left: 150px; }
  .contacts li { display: flex; align-items: center; gap: 9px; height: 15.5px; }
  .contacts svg { width: 10px; height: 10px; fill: var(--text-muted); flex: none; }
</style>
</head>
<body>
<main class="stage">

  <section class="card card--front" aria-label="Card front">
    <div class="wordmark">
      <span class="wordmark__main">HARLOW</span>
      <span class="wordmark__sub">TUBULAR SERVICES</span>
    </div>
    <div class="service-band">
      <span>LAYDOWN MACHINE</span><span>|</span>
      <span>CASING CREW</span><span>|</span>
      <span>MUD TOOL</span><span>|</span>
      <span>TORQUE TURN</span>
    </div>
    <div class="website-line">
      <svg class="rule" viewBox="0 0 82 4" aria-hidden="true"><path d="M0 2 L82 0.5 L82 3.5 Z" fill="var(--brand-red)"/></svg>
      <span>www.harlowtubular.com</span>
      <svg class="rule" viewBox="0 0 82 4" aria-hidden="true"><path d="M82 2 L0 0.5 L0 3.5 Z" fill="var(--brand-red)"/></svg>
    </div>
  </section>

  <section class="card card--back" aria-label="Card back">
    <svg class="back-curve" viewBox="0 0 484 292" preserveAspectRatio="none" aria-hidden="true">
      <path d="M112 0 C152 0 168 90 206 136 C244 180 330 190 484 206 L484 0 Z" fill="var(--brand-red)"/>
      <path d="M128 0 C164 0 182 88 218 130 C256 172 336 186 484 202 L484 0 Z" fill="var(--card-white)"/>
    </svg>

    <div class="wordmark">
      <span class="wordmark__main">HARLOW</span>
      <span class="wordmark__sub">TUBULAR SERVICES</span>
    </div>

    <div class="holder">
      <p class="holder__name">Wade Kessler</p>
      <p class="holder__title">Area Manager</p>
    </div>

    <ul class="contacts contacts--phones">
      <li><svg viewBox="0 0 10 10"><path d="M2 0.5 L3.6 2.6 L2.8 3.6 C3.4 5 4.9 6.5 6.4 7.2 L7.4 6.4 L9.5 8 L8.4 9.5 C4.5 9.3 0.7 5.5 0.5 1.6 Z"/></svg>(555) 214-6300</li>
      <li><svg viewBox="0 0 10 10"><path d="M0.5 3 C2 1 8 1 9.5 3 L9.5 4.3 L7.4 4.3 L7.2 3.3 L2.8 3.3 L2.6 4.3 L0.5 4.3 Z M2 5 L8 5 L9 9 L1 9 Z"/></svg>(555) 382-9174</li>
      <li><svg viewBox="0 0 10 10"><path d="M2.5 0.5 H7.5 V3 H2.5 Z M0.5 3.5 H9.5 V7.5 H8 V6 H2 V7.5 H0.5 Z M2.5 6.5 H7.5 V9.5 H2.5 Z"/></svg>(555) 214-6310</li>
    </ul>

    <ul class="contacts contacts--details">
      <li><svg viewBox="0 0 10 10"><path d="M5 0 C7.3 0 8.6 1.7 8.6 3.6 C8.6 6 5 10 5 10 C5 10 1.4 6 1.4 3.6 C1.4 1.7 2.7 0 5 0 Z M5 2.2 A1.4 1.4 0 1 0 5 5 A1.4 1.4 0 1 0 5 2.2 Z"/></svg>Ridgeport, OK 73000</li>
      <li><svg viewBox="0 0 10 10"><path d="M0.5 2 H9.5 V8.5 H0.5 Z M1.2 2.6 L5 5.6 L8.8 2.6" stroke="var(--slate)" stroke-width="0.8"/></svg>wadekessler@harlowtubular.com</li>
      <li><svg viewBox="0 0 10 10"><circle cx="5" cy="5" r="4.5"/><path d="M0.5 5 H9.5 M5 0.5 C3 3 3 7 5 9.5 M5 0.5 C7 3 7 7 5 9.5" stroke="var(--slate)" stroke-width="0.7" fill="none"/></svg>www.harlowtubular.com</li>
    </ul>
  </section>

</main>
</body>
</html>
```